Corvanta Business cards template

We're looking for something modern and elegant. We are a reseller of technology (computers, datacenter, etc). Color theme would be "only" white with the incorporation of the blue that's present on our website (Corvanta.com) and logo file. We would like for the card to provide all the necessary info for the specific person (Phone#, fax#, email, name, website URL) . I'm attaching the logo file to this request. Please have it show Northvale/Eastbrook somewhere, without providing specific addresses.

Target Market(s)

All b2b

Industry/Entity Type

Business

Contact Information for Business Card

Please have the color scheme be represented by only the white and blue from our website (Corvanta.com) and logo. We would like to logo on the card, but not big and overwhelming. This card will be used as a template for anybody within the company, it should display the user's name, phone#, fax#, email, job title and website URL. Please have it show Northvale/Eastbrook somewhere, without providing our specific addresses. Really, we're looking for a clean, simple and elegant look.

Font styles to use
Serif

Requirements
Must have
• Please see card details
Nice to have
• Please see card details
Should not have
• Anything tacky or tagline.

```html
<!DOCTYPE html>
<html lang="en">
<head>
<meta charset="utf-8">
<title>Corvanta Business Card</title>
<link rel="stylesheet" href="https://fonts.googleapis.com/css2?family=Exo+2:wght@300;400;500;700&display=swap">
<style>
  :root {
    --brand-blue: #1a78c8;
    --brand-blue-deep: #0d5ea8;
    --brand-blue-light: #3191dc;
    --card-white: #ffffff;
    --text-dark: #3a3f45;
    --rule-grey: #9aa3ab;
    --page-bg: #e9ebee;
  }
  * { box-sizing: border-box; margin: 0; padding: 0; }
  html, body {
    width: 1200px; height: 1024px; overflow: hidden;
    background: var(--page-bg);
    font-family: "Exo 2", sans-serif;
  }
  .sheet {
    width: 1200px; height: 1024px;
    display: flex; flex-direction: column; align-items: center; justify-content: center; gap: 64px;
  }
  .card {
    width: 700px; height: 400px; position: relative;
    box-shadow: 0 6px 20px rgba(0,0,0,0.18);
  }
  .card-front { background: var(--card-white); }
  .card-back {
    background: linear-gradient(135deg, var(--brand-blue-light) 0%, var(--brand-blue) 50%, var(--brand-blue-deep) 100%);
  }
  .wordmark {
    font-family: "Exo 2", sans-serif; font-weight: 300; letter-spacing: 1px;
    display: flex; align-items: center; gap: 12px; white-space: nowrap;
  }
  .wordmark-dot { width: 14px; height: 14px; border-radius: 50%; flex: none; }
  .card-front .wordmark { position: absolute; left: 50px; top: 100px; font-size: 62px; line-height: 1; color: var(--brand-blue); }
  .card-front .wordmark-dot { background: var(--brand-blue); }
  .divider {
    position: absolute; left: 30px; right: 30px; top: 196px; height: 1px; background: var(--rule-grey);
  }
  .holder-name {
    position: absolute; right: 40px; top: 152px;
    font-size: 30px; font-weight: 500; color: var(--brand-blue); letter-spacing: 0.5px; white-space: nowrap;
  }
  .holder-title {
    position: absolute; right: 40px; top: 204px;
    font-size: 15px; font-weight: 400; color: var(--brand-blue); letter-spacing: 0.5px; white-space: nowrap;
  }
  .contact-list { list-style: none; position: absolute; font-size: 17px; color: var(--text-dark); letter-spacing: 1px; }
  .contact-list li { display: flex; align-items: center; gap: 10px; height: 27px; white-space: nowrap; }
  .contact-list svg { width: 15px; height: 15px; fill: var(--brand-blue); flex: none; }
  .phone-list { left: 50px; top: 252px; }
  .details-list { left: 430px; top: 242px; }
  .card-back .wordmark {
    position: absolute; left: 50%; top: 50%; transform: translate(-50%, -50%);
    font-size: 72px; color: var(--card-white);
  }
  .card-back .wordmark-dot { background: var(--card-white); }
  .back-url {
    position: absolute; left: 60px; bottom: 60px;
    font-size: 16px; color: var(--card-white); letter-spacing: 1px;
  }
</style>
</head>
<body>
<main class="sheet">
  <section class="card card-front" aria-label="Card front">
    <div class="wordmark"><span class="wordmark-dot"></span>Corvanta</div>
    <div class="holder-name">Adrian Kessler</div>
    <div class="divider"></div>
    <div class="holder-title">Managing Director</div>
    <ul class="contact-list phone-list">
      <li><svg viewBox="0 0 16 16" aria-hidden="true"><path d="M3 1h3l1.5 4-2 1.3a9 9 0 0 0 4.2 4.2L11 8.5l4 1.5v3a2 2 0 0 1-2 2A12 12 0 0 1 1 3a2 2 0 0 1 2-2z"/></svg>(555) 214-7730</li>
      <li><svg viewBox="0 0 16 16" aria-hidden="true"><path d="M4 0h8a1 1 0 0 1 1 1v14a1 1 0 0 1-1 1H4a1 1 0 0 1-1-1V1a1 1 0 0 1 1-1zm1 2v10h6V2z"/></svg>(555) 214-7731</li>
      <li><svg viewBox="0 0 16 16" aria-hidden="true"><path d="M4 0h8v5H4zM1 6h14v8H1zm3 2v2h8V8z"/></svg>(555) 390-4182</li>
    </ul>
    <ul class="contact-list details-list">
      <li><svg viewBox="0 0 16 16" aria-hidden="true"><path d="M1 3h14v10H1zm1.5 1.5V5l5.5 4 5.5-4v-.5z"/></svg>name@Corvanta.com</li>
      <li><svg viewBox="0 0 16 16" aria-hidden="true"><path d="M8 0a8 8 0 1 1 0 16A8 8 0 0 1 8 0zm0 2a6 6 0 1 0 0 12A6 6 0 0 0 8 2zM2 7.5h12v1H2zM7.5 2h1v12h-1z"/></svg>www.Corvanta.com</li>
      <li><svg viewBox="0 0 16 16" aria-hidden="true"><path d="M8 0a5 5 0 0 1 5 5c0 4-5 11-5 11S3 9 3 5a5 5 0 0 1 5-5zm0 3a2 2 0 1 0 0 4 2 2 0 0 0 0-4z"/></svg>Northvale/Eastbrook</li>
    </ul>
  </section>

  <section class="card card-back" aria-label="Card back">
    <div class="wordmark"><span class="wordmark-dot"></span>Corvanta</div>
    <div class="back-url">www.Corvanta.com</div>
  </section>
</main>
</body>
</html>
```